Book cover - Quiet Rooms, Open Doors

Book cover for Ebook (Pagelight) and wrap around print cover (Printvale) (back, front, and spine)

The book title (may slightly change by end of brief):
(MAIN TITLE) 'Quiet Rooms, Open Doors'
(SUB HEADING) 'A Week-by-Week Practical Workbook to Loosen Nervous Habits, Quieten Doubt and Build Steady Poise'
by Dr Owen Hartley

I would like a bold, stand out cover. Contemporary. I would like to avoid stereotypical images of people looking anxious or worried. I would like the design to be more uplifting and hopeful, rather than focusing on the negative aspect of anxiety, but avoiding cliched photos of people raising their hands in the air, smiling and jumping etc. The cover should appeal to both men and women.

Trim size of book cover (for PrintVale) is 5.25" x 8" back and front with a spine size of 0.477 inches

Reason: I have decided to extend the deadline by 1 more day, not because I am unhappy with the quality of the designs, but because a few designers have contacted me to explain they have had technical difficulties when submitting their files. Thanks everyone for the hard work and great designs.

Target Market(s)

Males and females (16+) who struggle with social anxiety and shyness

Industry/Entity Type

Social

Font styles to use
Serif

Requirements
Must have
• Bold cover that is modern and contemporary. For example, I like these covers:
• http://shrtlnk.example/k4Tq9Zb
• http://shrtlnk.example/m8Wv2Hn
• http://shrtlnk.example/p3Jx6Lr
• http://shrtlnk.example/t7Gd1Qe
• http://shrtlnk.example/v2Nk8Fy
• http://shrtlnk.example/w9Bh4Cs
• http://shrtlnk.example/z5Mf3Ud
Nice to have
• Open to abstract designs.
Should not have
• No stereotypical pictures of people who look anxious or worried. Avoid cliched photos of people raising their hands in the air, smiling and jumping etc.

```html
<!DOCTYPE html>
<html lang="en">
<head>
<meta charset="utf-8">
<title>Quiet Rooms, Open Doors – Book Cover</title>
<link rel="stylesheet" href="https://fonts.googleapis.com/css2?family=Cinzel:wght@400;500&display=swap">
<style>
  :root {
    --page-bg: #ffffff;
    --cover-bg: #ffffff;
    --cover-edge: #3a3a3a;
    --title-crimson: #c4114d;
    --subtitle-green: #3f7d14;
    --author-navy: #1d4e8a;
    --art-yellow: #f2d21a;
    --art-green: #7cc52a;
    --art-orange: #f27a12;
    --art-magenta: #d9278a;
    --art-violet: #9a3aa6;
    --art-blue: #1f8fd0;
  }
  * { margin: 0; padding: 0; box-sizing: border-box; }
  html, body {
    width: 1200px;
    height: 1200px;
    overflow: hidden;
    background: var(--page-bg);
  }
  .canvas {
    position: relative;
    width: 1200px;
    height: 1200px;
  }
  .book-cover {
    position: absolute;
    left: 401px;
    top: 345px;
    width: 324px;
    height: 494px;
    background: var(--cover-bg);
    border: 1px solid var(--cover-edge);
    font-family: "Cinzel", "Times New Roman", serif;
    text-align: center;
  }
  .cover-title {
    position: absolute;
    top: 24px;
    left: 0;
    width: 100%;
    color: var(--title-crimson);
    font-weight: 400;
    white-space: nowrap;
  }
  .cover-title .line {
    display: block;
  }
  .cover-title .line-one {
    font-size: 36px;
    line-height: 44px;
  }
  .cover-title .line-two {
    font-size: 40px;
    line-height: 46px;
  }
  .cover-subtitle {
    position: absolute;
    top: 140px;
    left: 0;
    width: 100%;
    color: var(--subtitle-green);
    font-size: 13px;
    line-height: 17px;
    font-weight: 400;
  }
  .cover-subtitle span {
    display: block;
  }
  .cover-art {
    position: absolute;
    left: 10px;
    top: 231px;
    width: 296px;
    height: 215px;
  }
  .cover-author {
    position: absolute;
    top: 448px;
    left: 0;
    width: 100%;
    color: var(--author-navy);
    font-size: 30px;
    line-height: 34px;
    font-weight: 400;
    white-space: nowrap;
  }
</style>
</head>
<body>
  <div class="canvas">
    <section class="book-cover">
      <h1 class="cover-title">
        <span class="line line-one">Quiet Rooms,</span>
        <span class="line line-two">Open Doors</span>
      </h1>
      <p class="cover-subtitle">
        <span>A Week-by-Week</span>
        <span>Practical Workbook</span>
        <span>to Loosen Nervous Habits,</span>
        <span>Quieten Doubt</span>
        <span>and Build Steady Poise</span>
      </p>
      <svg class="cover-art" viewBox="0 0 296 215" role="img" aria-label="Watercolour illustration of four figures in bright yellow, orange, magenta and blue tones">
        <defs>
          <linearGradient id="artWash" x1="0" y1="0" x2="1" y2="0">
            <stop offset="0" stop-color="var(--art-yellow)"/>
            <stop offset="0.2" stop-color="var(--art-green)"/>
            <stop offset="0.38" stop-color="var(--art-orange)"/>
            <stop offset="0.6" stop-color="var(--art-magenta)"/>
            <stop offset="0.75" stop-color="var(--art-violet)"/>
            <stop offset="1" stop-color="var(--art-blue)"/>
          </linearGradient>
          <linearGradient id="artFade" x1="0" y1="0" x2="0" y2="1">
            <stop offset="0" stop-color="#fff" stop-opacity="0.55"/>
            <stop offset="0.35" stop-color="#fff" stop-opacity="0"/>
            <stop offset="0.8" stop-color="#fff" stop-opacity="0"/>
            <stop offset="1" stop-color="#fff" stop-opacity="0.5"/>
          </linearGradient>
        </defs>
        <rect x="0" y="0" width="296" height="215" rx="18" fill="url(#artWash)"/>
        <rect x="0" y="0" width="296" height="215" rx="18" fill="url(#artFade)"/>
      </svg>
      <p class="cover-author">Dr Owen Hartley</p>
    </section>
  </div>
</body>
</html>
```